Brightstep Podiatry Needs a Branded 8.5 x 11 template

We need a single template that will reflect our brand and have a really interesting and catchy feel. Be creative. It should include our logo a catch phrase like "Where Your Feet Are in Good Hands" and editable. There should be a header with this information. The central portion should be available to place text about medical conditions or other information and available to take pictures.
The footer needs to be all of the info on our location such as address, phone, drs names etc. - see must haves
We like shadows, 3D, really creative and catchy.
Below is an example that my friend uses. I like it but would like something a little more interesting. I do not want the same design as the flyer attached.
Logo is attached.
Our Colors: Want plenty of white space
#FAC000
#9F38AA

Target Market(s)

Patients and Physicians. We are podiatrists, foot and ankle specialists but I do not want any pictures of feet or medical stuff on the template.

Industry/Entity Type

Medical

Requirements
Must have
• For the Footer: Make it creative please

Physicians and Surgeons of the Foot and Ankle
Dr. Owen Pruitt
Dr. Carla Wendham
Address 4726 W. Bellrose Ave. Suite 418, Tampa, FL 33614
phone - 813-642-0917
email office@brightsteppodiatrymail.com
web http://www.theGulfcrestFootDoc.com

The Tagline section in the header needs to be editable so I can make changes. The middle section also needs to be editable.

I prefer to make edits in Photoshop or possibly Illustrator

```html
<!DOCTYPE html>
<html lang="en">
<head>
<meta charset="utf-8">
<title>Brightstep Podiatry – Newsletter Template</title>
<link href="https://fonts.googleapis.com/css2?family=Arimo:wght@400;700&family=Kalam:wght@700&display=swap" rel="stylesheet">
<style>
  :root {
    --purple: #9F38AA;
    --purple-deep: #7d2288;
    --yellow: #FAC000;
    --yellow-soft: #f3cf72;
    --ink: #1e1e1e;
    --white: #ffffff;
    --photo-tone: #a7b48c;
  }
  * { margin: 0; padding: 0; box-sizing: border-box; }
  html, body { width: 927px; height: 1200px; overflow: hidden; background: var(--white); }
  .page {
    position: relative; width: 927px; height: 1200px; overflow: hidden;
    background: var(--white); font-family: "Arimo", Arial, sans-serif; color: var(--ink);
  }
  .header-bg { position: absolute; left: 0; top: 0; width: 927px; height: 290px; }
  .logo-card {
    position: absolute; left: 213px; top: 0; width: 494px; height: 157px;
    background: var(--white); box-shadow: 0 6px 14px rgba(0,0,0,.35);
    display: flex; align-items: center; justify-content: center; gap: 14px;
  }
  .logo-dot { width: 22px; height: 22px; border-radius: 50%; background: var(--purple); }
  .logo-name { font-size: 40px; font-weight: 400; color: var(--ink); white-space: nowrap; }
  .tagline {
    position: absolute; top: 186px; left: 0; width: 927px; text-align: center;
    font-family: "Kalam", "Comic Sans MS", cursive; font-weight: 700;
    font-size: 35px; line-height: 48px; color: var(--yellow);
    text-shadow: 0 1px 2px rgba(0,0,0,.25); white-space: nowrap;
  }
  .section-title {
    position: absolute; left: 73px; font-size: 31.5px; line-height: 38px;
    font-weight: 400; color: var(--ink); white-space: nowrap;
  }
  .body-copy {
    position: absolute; font-size: 15.3px; line-height: 21.3px;
    hyphens: auto; -webkit-hyphens: auto;
  }
  .body-copy.justified { text-align: justify; }
  .body-copy p + p { margin-top: 21.3px; }
  .article-photo {
    position: absolute; left: 478px; top: 347px; width: 418px; height: 229px;
    background: var(--photo-tone);
  }
  .footer {
    position: absolute; left: 0; top: 1038px; width: 927px; height: 162px;
    background: linear-gradient(180deg, var(--purple) 0%, var(--purple-deep) 100%);
    color: var(--white);
  }
  .doctors {
    position: absolute; left: 24px; top: 19px; font-size: 22.5px; line-height: 26px;
    font-weight: 700; white-space: nowrap;
  }
  .specialty {
    position: absolute; left: 24px; top: 44px; font-size: 17px; line-height: 18px;
    color: var(--yellow); font-variant: small-caps; letter-spacing: .4px; white-space: nowrap;
  }
  .contact-list { position: absolute; left: 24px; top: 66px; list-style: none; }
  .contact-list li {
    display: flex; align-items: center; gap: 14px; height: 21.3px;
    font-size: 17px; white-space: nowrap;
  }
  .contact-list svg { width: 14px; height: 14px; fill: var(--yellow); flex: none; }
  .footer-brand {
    position: absolute; left: 524px; top: 62px; display: flex; align-items: center; gap: 12px;
  }
  .footer-brand .logo-dot { background: var(--white); width: 18px; height: 18px; }
  .footer-brand .logo-name { color: var(--white); font-size: 36px; }
</style>
</head>
<body>
<div class="page">
  <svg class="header-bg" viewBox="0 0 927 290" preserveAspectRatio="none" aria-hidden="true">
    <path d="M0 0 H927 V250 C700 242 420 240 0 284 Z" fill="var(--yellow-soft)"/>
    <path d="M0 0 H927 V244 C700 236 420 236 0 262 Z" fill="var(--yellow)"/>
    <path d="M0 0 H927 V228 C640 232 330 238 0 238 Z" fill="var(--purple)"/>
  </svg>

  <header>
    <div class="logo-card">
      <span class="logo-name">Brightstep Podiatry</span>
      <span class="logo-dot"></span>
    </div>
    <div class="tagline">Where Your Feet Are in Good Hands</div>
  </header>

  <main>
    <h2 class="section-title" style="top:301px">Running Shoes: How to Choose</h2>
    <div class="body-copy" style="left:24px; top:350px; width:421px">
      <p>While most running shoes feel comfortable when you're standing in a sports store, the true test is after several miles on the trail or asphalt. You'll quickly realize that your perfect shoe has more to do with the shape of your foot and your running style than it does with the logo stitched on the side.</p>
      <p>This article discusses how to narrow down your traditional running shoe choices. For a look at the increasingly popular minimalist shoe styles, see the companion Trailwise Expert Advice</p>
    </div>
    <div class="article-photo" role="img" aria-label="Article photo area"></div>

    <h2 class="section-title" style="top:631px">Common Foot &amp; Ankle Disorders</h2>
    <div class="body-copy justified" style="left:24px; top:684px; width:421px">
      <p>The most common cause of yellowed, thick and /or deformed toenails is a fungal infection of the toenail. The fungus that infects the nail, most commonly, is the same fungus that causes athletes foot. It tends to be slowly progressive, damaging the nail to a greater and greater degree over time. The infection usually starts at the tip of the nail and works its way back. It usually is not painful and often not noticed until it has gotten well established. A single toenail or any number of nails can be affected. It can also occur on just one foot. Over time, the nail becomes thickened, crumbly, and distorted in appearance. Sweaty feet contribute to the initial infection process and contribute to its spread. The fungus prefers an environment that is moist, dark, and warm, which is why it affects the toenails much more often than fingernails.</p>
    </div>
    <div class="body-copy justified" style="left:475px; top:684px; width:427px">
      <p>It does not spread through the blood stream. The infection limits itself to the nails and skin. It is often found in association with areas of dry scaly skin on the bottom of the foot or between the toes. The dry scaling skin is frequently found to be chronic athletes' foot. It is not highly contagious, and family members are almost as likely to contract it from some other source as they are from the family member who has the infection. Keeping common showering areas clean is recommended, and sharing shoes should be avoided..</p>
    </div>
  </main>

  <footer class="footer">
    <div class="doctors">Dr. Owen Pruitt &amp; Dr. Carla Wendham</div>
    <div class="specialty">Physicians and Surgeons of the Foot and Ankle</div>
    <ul class="contact-list">
      <li><svg viewBox="0 0 24 24"><path d="M12 2a7 7 0 0 0-7 7c0 5 7 13 7 13s7-8 7-13a7 7 0 0 0-7-7zm0 9.5A2.5 2.5 0 1 1 12 6a2.5 2.5 0 0 1 0 5.5z"/></svg>4726 W. Bellrose Ave. Suite 418, Tampa, FL 33614</li>
      <li><svg viewBox="0 0 24 24"><path d="M6.6 10.8a15 15 0 0 0 6.6 6.6l2.2-2.2c.3-.3.7-.4 1-.2 1.1.4 2.3.6 3.6.6.6 0 1 .4 1 1V20c0 .6-.4 1-1 1A17 17 0 0 1 3 4c0-.6.4-1 1-1h3.5c.6 0 1 .4 1 1 0 1.3.2 2.5.6 3.6.1.3 0 .7-.2 1z"/></svg>813-642-0917</li>
      <li><svg viewBox="0 0 24 24"><path d="M2 5h20v14H2z M3.5 6.5v.4l8.5 6 8.5-6v-.4z" fill-rule="evenodd"/></svg>office@brightsteppodiatrymail.com</li>
      <li><svg viewBox="0 0 24 24"><path d="M4 14 14 4l6 6-10 10H4z"/></svg>www.theGulfcrestFootDoc.com</li>
    </ul>
    <div class="footer-brand">
      <span class="logo-name">Brightstep Podiatry</span>
      <span class="logo-dot"></span>
    </div>
  </footer>
</div>
</body>
</html>
```